PRVKA Membership Flyer

• 1 Page Flyer promoting PRVKA Membership Drive
• I have attached our organization brochure for organizational info
• Please include the same PRVKA logo as seen in brochure
• Membership $20/year
• Contact Tomas Weller to Join at wellto42@learners.brvx.edu
INCLUDE Organization Advisers
Dr. Rostam Velani NPV School of Dental Medicine (photo from attached brochure)
Dr. Felix Oyo NPV Tarrow School of Medicine (Photo from Attached brochure)

Member Benefits
• Access to exclusive Interdisciplinary world-renowned guest speaker presentations
• Mentorship for residencies / Oral Medicine Fellowship for nondental healthcare students
• Shadowing opportunities with Oral Medicine Specialist
• Participate in research journal club
• Clinical Research, Case Reports and Lindqvar Fellowship opportunities
• Exclusive Lunch and Learn Invitations
• 10% Discount to Special Events Sponsored by PRVKA
• Enhance your Interdisciplinary resource network

Renew or Join PRVKA by August 30th and be entered in a free raffle for the chance to win one of 3 drawings
$50 Zorel Gift Card
2x $25 Plumfield Gift Card

Target Market(s)

Students

Requirements
Must have
• Must use the PRVKA Logo from brochure, Member Benefits • Access to exclusive Interdisciplinary world-renowned guest speaker presentations • Mentorship for residencies / Oral Medicine Fellowship for nondental healthcare students • Shadowing opportunities with Oral Medicine Specialist • Participate in research journal club • Clinical Research, Case Reports and Lindqvar Fellowship opportunities • Exclusive Lunch and Learn Invitations • 10% Discount to Special Events Sponsored by PRVKA • Enhance your Interdisciplinary resource network Renew or Join PRVKA by August 30th and be entered in a free raffle for the chance to win one of 3-4 drawings $50 Zorel Gift Card 2x $25 Plumfield Gift Card
Nice to have
• Similar design background to brochure attached,

```html
<!DOCTYPE html>
<html lang="en">
<head>
<meta charset="utf-8">
<title>PRVKA Membership Flyer</title>
<link href="https://fonts.googleapis.com/css2?family=Poppins:wght@300;400;600;700;800&family=Source+Serif+4:wght@400;600;700&display=swap" rel="stylesheet">
<style>
  :root {
    --purple: #53307f;
    --gold: #c7a848;
    --paper: #f3f3f4;
    --ink: #2b2b2b;
    --rule: #8d8d8d;
    --stage: #d6d5da;
    --sketch: #e2e2e4;
    --photo: #7a7a80;
  }
  * { margin: 0; padding: 0; box-sizing: border-box; }
  html, body { width: 1135px; height: 1200px; overflow: hidden; }
  body { background: var(--stage); position: relative; }

  .flyer {
    position: absolute; left: 111px; top: 0;
    width: 788px; height: 1037px;
    background: var(--paper);
    transform: scale(1.1572); transform-origin: 0 0;
    font-family: "Source Serif 4", Georgia, serif;
    color: var(--ink);
  }

  .hero-art {
    position: absolute; left: 0; top: 0; width: 440px; height: 285px;
    background: radial-gradient(ellipse at 45% 45%, var(--sketch) 0%, rgba(243,243,244,0) 70%);
  }

  .brand {
    position: absolute; left: 458px; top: 124px; width: 260px; height: 70px;
    display: flex; align-items: center; justify-content: center; gap: 12px;
  }
  .brand .dot { width: 26px; height: 26px; border-radius: 50%; background: var(--purple); flex: none; }
  .brand .name {
    font-family: "Poppins", sans-serif; font-weight: 600; font-size: 52px; line-height: 70px;
    color: var(--purple); white-space: nowrap;
  }

  .adviser { position: absolute; top: 302px; }
  .adviser .photo { position: absolute; left: 0; top: 0; width: 76px; height: 99px; background: linear-gradient(#8c8c92, var(--photo)); }
  .adviser .name {
    position: absolute; left: 89px; top: 14px; white-space: nowrap;
    font-family: "Poppins", sans-serif; font-weight: 600; font-size: 20px; color: var(--purple);
  }
  .adviser .rule { position: absolute; left: 89px; top: 51px; width: 232px; height: 1px; background: var(--rule); }
  .adviser .school { position: absolute; left: 89px; top: 62px; font-size: 15.5px; font-weight: 600; white-space: nowrap; }
  .adviser.left { left: 61px; }
  .adviser.right { left: 403px; }
  .adviser.right .name, .adviser.right .rule, .adviser.right .school { left: 91px; }

  .benefits-bar {
    position: absolute; left: 61px; top: 427px; width: 665px; height: 33px;
    background: var(--gold); color: #fff; text-align: center;
    font-family: "Poppins", sans-serif; font-weight: 700; font-size: 25px; line-height: 35px;
  }
  .benefits { position: absolute; top: 471px; list-style: none; }
  .benefits.col-a { left: 86px; width: 272px; }
  .benefits.col-b { left: 415px; width: 272px; }
  .benefits li {
    position: relative; padding-left: 22px; margin-bottom: 6px;
    font-size: 14.2px; line-height: 17px;
  }
  .benefits li svg { position: absolute; left: 0; top: 2px; width: 14px; height: 14px; }

  .membership {
    position: absolute; left: 0; top: 646px; width: 788px; height: 327px; background: var(--purple);
  }
  .price {
    position: absolute; left: 58px; top: 20px; white-space: nowrap;
    font-family: "Poppins", sans-serif; font-size: 45px; line-height: 60px; color: var(--gold);
  }
  .price .label { font-weight: 400; letter-spacing: -1px; }
  .price .amount { font-weight: 700; }
  .contact {
    position: absolute; left: 58px; top: 80px; width: 672px; color: #fff;
    font-family: "Poppins", sans-serif; font-weight: 600; font-size: 17.5px;
  }
  .contact .email { position: absolute; left: 342px; top: 0; }
  .dash { position: absolute; left: 58px; width: 672px; border-top: 1.5px dashed #cfc6dc; }
  .dash.one { top: 123px; }
  .dash.two { top: 196px; }
  .raffle {
    position: absolute; left: 0; top: 135px; width: 788px; text-align: center; color: var(--gold);
    font-family: "Poppins", sans-serif; font-weight: 600; font-size: 17.5px; line-height: 24px;
  }
  .prize { position: absolute; top: 210px; text-align: center; }
  .prize .big {
    color: #fff; font-family: "Poppins", sans-serif; font-weight: 700;
    font-size: 64px; line-height: 80px; letter-spacing: -2px; white-space: nowrap;
  }
  .prize .ribbon {
    margin: -8px auto 0; height: 21px; background: var(--gold); color: #fff;
    font-weight: 700; font-size: 16px; line-height: 21px;
    clip-path: polygon(0 0, 100% 0, 96% 50%, 100% 100%, 0 100%, 4% 50%);
  }
  .prize.drawings { left: 58px; width: 184px; }
  .prize.cafe { left: 278px; width: 228px; }
  .prize.card { left: 545px; width: 184px; }

  .website {
    position: absolute; left: 0; top: 995px; width: 788px; text-align: center;
    font-family: "Poppins", sans-serif; font-weight: 700; font-size: 18px; letter-spacing: 4.6px; color: var(--ink);
  }
</style>
</head>
<body>
  <main class="flyer">
    <div class="hero-art" role="img" aria-label="Light grey line sketch of two hands clasped in a handshake"></div>

    <div class="brand"><span class="dot"></span><span class="name">PRVKA</span></div>

    <section class="adviser left">
      <div class="photo" role="img" aria-label="Portrait photo of Dr. Rostam Velani"></div>
      <h2 class="name">Dr. Rostam Velani NPV</h2>
      <div class="rule"></div>
      <p class="school">School of Dental Medicine</p>
    </section>
    <section class="adviser right">
      <div class="photo" role="img" aria-label="Portrait photo of Dr. Felix Oyo"></div>
      <h2 class="name">Dr. Felix Oyo NPV</h2>
      <div class="rule"></div>
      <p class="school">Tarrow School of Medicine</p>
    </section>

    <h2 class="benefits-bar">Member Benefits</h2>
    <ul class="benefits col-a">
      <li><svg viewBox="0 0 14 14"><circle cx="7" cy="7" r="5.5" fill="none" stroke="#53307f" stroke-width="1.6"/><path d="M4 7l2.3 2.3L12.5 2.5" fill="none" stroke="#c7a848" stroke-width="1.8"/></svg>Access to exclusive Interdisciplinary world-renowned guest speaker presentations</li>
      <li><svg viewBox="0 0 14 14"><circle cx="7" cy="7" r="5.5" fill="none" stroke="#53307f" stroke-width="1.6"/><path d="M4 7l2.3 2.3L12.5 2.5" fill="none" stroke="#c7a848" stroke-width="1.8"/></svg>Mentorship for residencies / Oral Medicine Fellowship for nondental healthcare students</li>
      <li><svg viewBox="0 0 14 14"><circle cx="7" cy="7" r="5.5" fill="none" stroke="#53307f" stroke-width="1.6"/><path d="M4 7l2.3 2.3L12.5 2.5" fill="none" stroke="#c7a848" stroke-width="1.8"/></svg>Shadowing opportunities with Oral Medicine Specialist</li>
    </ul>
    <ul class="benefits col-b">
      <li><svg viewBox="0 0 14 14"><circle cx="7" cy="7" r="5.5" fill="none" stroke="#53307f" stroke-width="1.6"/><path d="M4 7l2.3 2.3L12.5 2.5" fill="none" stroke="#c7a848" stroke-width="1.8"/></svg>Participate in research journal club</li>
      <li><svg viewBox="0 0 14 14"><circle cx="7" cy="7" r="5.5" fill="none" stroke="#53307f" stroke-width="1.6"/><path d="M4 7l2.3 2.3L12.5 2.5" fill="none" stroke="#c7a848" stroke-width="1.8"/></svg>Clinical Research, Case Reports and Lindqvar Fellowship opportunities</li>
      <li><svg viewBox="0 0 14 14"><circle cx="7" cy="7" r="5.5" fill="none" stroke="#53307f" stroke-width="1.6"/><path d="M4 7l2.3 2.3L12.5 2.5" fill="none" stroke="#c7a848" stroke-width="1.8"/></svg>Exclusive Lunch and Learn Invitations</li>
      <li><svg viewBox="0 0 14 14"><circle cx="7" cy="7" r="5.5" fill="none" stroke="#53307f" stroke-width="1.6"/><path d="M4 7l2.3 2.3L12.5 2.5" fill="none" stroke="#c7a848" stroke-width="1.8"/></svg>10% Discount to Special Events Sponsored by PRVKA</li>
      <li><svg viewBox="0 0 14 14"><circle cx="7" cy="7" r="5.5" fill="none" stroke="#53307f" stroke-width="1.6"/><path d="M4 7l2.3 2.3L12.5 2.5" fill="none" stroke="#c7a848" stroke-width="1.8"/></svg>Enhance your Interdisciplinary resource network</li>
    </ul>

    <section class="membership">
      <h1 class="price"><span class="label">MEMBERSHIP</span> <span class="amount">$20 PER YEAR</span></h1>
      <p class="contact">Contact Tomas Weller to Join at <span class="email">WELLTO42@LEARNERS.BRVX.EDU</span></p>
      <div class="dash one"></div>
      <p class="raffle">Renew Or Join PRVKA By August 30th And<br>Be Entered In A Free Raffle For Thechance To Win</p>
      <div class="dash two"></div>
      <div class="prize drawings"><div class="big">1 of 3</div><div class="ribbon">Drawings</div></div>
      <div class="prize cafe"><div class="big">2x $25</div><div class="ribbon">Plumfield Gift Card</div></div>
      <div class="prize card"><div class="big">$50</div><div class="ribbon">Zorel Gift Card</div></div>
    </section>

    <p class="website">WWW.LEARNERS.BRVX.EDU</p>
  </main>
</body>
</html>
```